Create a standard e-mail template for market research invitations.
Please follow attached layout.
E-mail template must be fully coded and uploaded to mailchimp account and fully tested before sign off.
Logos are uploaded. Our website is www.meetkestrelpod.co.uk . Please stick to corporate image.
Example content:
Previous example attached. Happy with this style design or something a bit different, but must stick to layout style (html template 1 doc.) also attached. Template should allow for placement of similar content to given example and be text editable.
Main left hand side of header must be readable text and not downloadable image only to increase readership and improve look when arriving in inbox.
Thanks
Target Market(s)
General consumers
Industry/Entity Type
Market Research

```html
<!DOCTYPE html>
<html lang="en">
<head>
<meta charset="utf-8">
<title>Kestrel Pod – Research Invitation</title>
<link href="https://fonts.googleapis.com/css2?family=Noto+Sans:wght@400;700&display=swap" rel="stylesheet">
<style>
  :root{
    --backdrop:#666666;
    --paper:#ffffff;
    --green:#8dc21f;
    --green-soft:#c6ea7e;
    --green-pale:#e4f4c6;
    --brown:#7b6a55;
    --body-text:#555555;
    --nav-text:#333333;
    --nav-rule:#6f7590;
    --footer-bg:#c8c8c8;
    --footer-text:#6b5a45;
    --photo-dark:#5e5e5e;
    --photo-light:#d9d9d9;
  }
  *{box-sizing:border-box;margin:0;padding:0}
  html,body{width:1200px;height:1047px;overflow:hidden;background:var(--backdrop)}
  body{font-family:"Noto Sans",sans-serif}
  .stage{width:1073px;height:936px;position:relative;transform:scale(1.11836);transform-origin:0 0}
  .email{position:absolute;left:224px;top:14px;width:600px;height:940px;background:var(--paper)}
  .header{position:relative;height:217px}
  .header-pattern{position:absolute;left:0;top:0}
  .brand{position:absolute;left:364px;top:30px;font-size:36px;font-weight:700;color:var(--brown);letter-spacing:-1px}
  .headline{position:absolute;left:18px;top:104px;width:300px;font-size:24px;line-height:32px;font-weight:700;color:var(--green)}
  .main{position:absolute;left:0;top:217px;width:600px;height:560px}
  .content{position:absolute;left:42px;top:30px;width:330px}
  .content h2{font-size:20px;line-height:29px;font-weight:700;color:var(--brown)}
  .benefits{margin:20px 0 0 29px;font-size:14.6px;line-height:20px;color:var(--body-text)}
  .benefits li{margin-bottom:0.5px}
  .events{margin-top:42px;font-size:14.6px;line-height:20px;color:var(--body-text)}
  .events-art{float:left;width:117px;height:104px;margin-right:0}
  .events h3{font-size:19px;font-weight:700;color:var(--brown);line-height:22px;margin:6px 0 18px}
  .sidebar{position:absolute;left:384px;top:0;width:216px}
  .nav a{display:block;height:33px;line-height:33px;padding-left:18px;background:var(--green-soft);color:var(--nav-text);text-decoration:none;font-size:14.6px;border-bottom:1px solid var(--nav-rule)}
  .nav a:first-child{border-top:1px solid var(--nav-rule)}
  .photo{display:block;margin:18px 0 0 18px;width:180px;height:240px;background:linear-gradient(110deg,var(--photo-dark),var(--photo-light) 60%,#a8a8a8)}
  .caption{margin:14px 0 0 18px;font-size:14.6px;line-height:20px;color:var(--brown)}
  .footer{position:absolute;left:0;top:777px;width:600px;height:170px;background:var(--footer-bg);padding:14px 18px;font-size:14.6px;line-height:20px;color:var(--footer-text)}
  .footer p{margin-bottom:14px}
  .footer a{color:var(--footer-text);font-weight:700}
  .footer .plain{color:#222;font-weight:400;text-decoration:none}
</style>
</head>
<body>
<div class="stage">
  <div class="email">
    <header class="header">
      <svg class="header-pattern" width="600" height="217" role="img" aria-label="Decorative school of green fish swimming diagonally across the header">
        <defs>
          <linearGradient id="shoal" x1="0" y1="0" x2="1" y2="1">
            <stop offset="0" stop-color="#dff0b8"/>
            <stop offset="1" stop-color="#c9e78c"/>
          </linearGradient>
        </defs>
        <path d="M40 0 H330 Q360 40 350 110 L300 120 Q180 90 120 60 Q60 40 40 0 Z" fill="url(#shoal)"/>
        <path d="M360 90 Q430 80 480 60 L600 40 V210 L470 215 Q400 160 360 90 Z" fill="url(#shoal)"/>
      </svg>
      <div class="brand">kestrelpod</div>
      <h1 class="headline">Get paid for your beautiful opinions!</h1>
    </header>

    <section class="main">
      <div class="content">
        <h2>Health and beauty companies need your expert opinion...</h2>
        <ul class="benefits">
          <li>Invitations to participate in focus groups, telephone interviews and online surveys.</li>
          <li>Earn up to £100 for an hour of your time.</li>
          <li>Give your views on how companies innovate, launch, package and price their products.</li>
          <li>There is no cost to register and your privacy is guaranteed.</li>
        </ul>
        <div class="events">
          <svg class="events-art" role="img" aria-label="Green fish illustration"><rect x="10" y="0" width="95" height="100" rx="30" fill="#cfe99a"/></svg>
          <h3>Upcoming Events</h3>
          The quick brown fox jumps over the lazy dog. The quick brown fox jumps over the lazy dog. The quick brown fox jumps over the lazy dog. The quick brown fox jumps over the lazy dog.
        </div>
      </div>

      <aside class="sidebar">
        <nav class="nav">
          <a href="#">Click Here to Register</a>
          <a href="#">FAQs</a>
          <a href="#">Kestrel Pod Website</a>
        </nav>
        <div class="photo" role="img" aria-label="Black and white portrait photo of a smiling young woman"></div>
        <p class="caption">Be a Kestrel! Share your opinions with us!</p>
      </aside>
    </section>

    <footer class="footer">
      <p>No longer wish to receive these emails? <a href="#">Unsubscribe</a>.</p>
      <p>You are receiving this email because...</p>
      <p>Copyright © 2012 Kestrel Pod Ltd, 14 Marlow Lane, Leeds LS7 3QT. All rights reserved.</p>
      <p>Click <a class="plain" href="#">here</a> to report this email as spam.</p>
    </footer>
  </div>
</div>
</body>
</html>
```